Business card design needed

Our company background is that we provides transfers to and from the airport, social & corporate events, weddings.
We are also available for charter for birthday party, wine tastings, concerts, anniversary, school balls etc.
Our business cards have to reflect that we have a professional company, they are our first contact and have to stand out from the other 'players' in the market.

Industry/Entity Type

School

Contact Information for Business Card

BRISTEL QDF, Laurent & Marisol, mob: 0427 381 594, PO Box 287, Tarrowin WA 6311, ABN 52 914 603 278, Lic 7169/5804,

Requirements
Must have
• Telephone number: 0427 381 594
Website: www.BRISTELQDF.com.au
postal address: PO Box 287, Tarrowin WA 6311
Licences: Lic 7169/5804

***If using the new photo (one with the bus and buildings behind it), if possible can the buildings be cropped out. Thanks
Nice to have
• would be nice to have the pics of the vehicle(s), preferred the Pel on the card but not too fussed.
Should not have
• Picture of vehicle we don't have in our fleet. (We ONLY have the Pellics and Rendak Ovaro mini bus)

```html
<!DOCTYPE html>
<html lang="en">
<head>
<meta charset="utf-8">
<title>Bristel – Luxury Car and Coach business card</title>
<link rel="stylesheet" href="https://fonts.googleapis.com/css2?family=Source+Sans+3:wght@400&family=Cormorant+Garamond:wght@400&display=swap">
<style>
  :root {
    --backdrop: #d9dbdd;
    --card-black: #050505;
    --card-white: #ffffff;
    --ink: #1a1a1a;
    --photo-light: #b9b9b9;
    --photo-dark: #4a4a4a;
  }
  * { margin: 0; padding: 0; box-sizing: border-box; }
  html, body { width: 1200px; height: 900px; overflow: hidden; }
  body {
    background: var(--backdrop);
    position: relative;
    font-family: "Source Sans 3", "Helvetica Neue", Arial, sans-serif;
  }
  .card {
    position: absolute;
    width: 750px;
    height: 462px;
    overflow: hidden;
  }
  .card--back {
    left: 438px; top: 422px;
    background: var(--card-black);
  }
  .card--front {
    left: 15px; top: 15px;
    background: var(--card-white);
  }
  .front-panel { position: absolute; inset: 0; }
  .vehicle-photo {
    position: absolute;
    left: 0; top: 205px;
    width: 455px; height: 257px;
    background: radial-gradient(ellipse at 50% 45%, var(--photo-light) 0%, #8d8d8d 45%, var(--photo-dark) 80%, var(--card-black) 100%);
    border-radius: 40% 40% 0 0 / 30% 30% 0 0;
  }
  .brand {
    position: absolute;
    color: var(--card-white);
    text-align: center;
  }
  .brand__name { font-weight: 400; line-height: 1; }
  .brand__tagline {
    font-family: "Cormorant Garamond", Georgia, serif;
    line-height: 1;
  }
  .card--front .brand { left: 40px; top: 28px; width: 420px; }
  .card--front .brand__name { font-size: 104px; letter-spacing: 2px; }
  .card--front .brand__tagline { font-size: 30px; margin-top: 22px; }
  .contact {
    position: absolute;
    right: 24px; top: 296px;
    text-align: right;
    color: var(--ink);
    font-size: 19px;
    line-height: 29.7px;
    list-style: none;
  }
  .emblem {
    position: absolute;
    left: 240px; top: 88px;
    width: 270px; height: 270px;
    border: 5px solid var(--card-white);
    border-radius: 50%;
  }
  .card--back .brand { left: 240px; top: 160px; width: 270px; }
  .card--back .brand__name { font-size: 50px; }
  .card--back .brand__tagline { font-size: 19px; margin-top: 8px; }
</style>
</head>
<body>
  <section class="card card--back" aria-label="Business card back">
    <div class="emblem"></div>
    <div class="brand">
      <div class="brand__name">Bristel</div>
      <div class="brand__tagline">Luxury Car and Coach</div>
    </div>
  </section>

  <section class="card card--front" aria-label="Business card front">
    <svg class="front-panel" width="750" height="462" viewBox="0 0 750 462" aria-hidden="true">
      <path d="M0 0 H425 C545 80 555 330 415 462 H0 Z" fill="var(--card-black)"/>
    </svg>
    <div class="vehicle-photo" role="img" aria-label="Black and white photo of a luxury sedan, front view"></div>
    <div class="brand">
      <div class="brand__name">Bristel</div>
      <div class="brand__tagline">Luxury Car and Coach</div>
    </div>
    <ul class="contact">
      <li>Telephone: 0427 381 594</li>
      <li>Address: PO Box 287,</li>
      <li>Tarrowin WA 6311</li>
      <li>Licences: Lic 7169/5804</li>
      <li>www.BRISTELQDF.com.au</li>
    </ul>
  </section>
</body>
</html>
```